Wein-Etiketten gesucht
Zielgruppe
Familien geführtes Weingut. eine neue Etikettenlinie soll das bisherige Wein Sortiment ergänzen.
Wein: eine 3er Serie aus rot weiss und rose modern ausgebaut
Plazierung: Online, im Getränke und Weinfachhandel.
Zielgruppe: Moderne Weintrinker
bisherige Weinlinien: www.kellbergwein.de
Aufgabenstellung
Das Etikett soll reduziert sein.
Etikettenformat b127mm h90mm kann ggf angepasst werden.
Weinflasche bordeaux farbe antik
Kapsel schwarz matt kann ggf auch angepasst werden.
die Pflichtangaben sollten am rechten Rand stehen. (das Etikett kann auch breiter als 127 sein, dann verschwinden diese aus dem Sichtbereich.) alternativ ist auch ein Rückenetikett denkbar.
Druck erfolgt im 4c ggf mit Heißfolienprägung Gold

```html
<!DOCTYPE html>
<html lang="de">
<head>
<meta charset="utf-8">
<title>Kellberg UNO Inicio – Etikett</title>
<link rel="stylesheet" href="https://fonts.googleapis.com/css2?family=Montserrat:wght@400;700&family=Barlow+Condensed:wght@300;400;500&display=swap">
<style>
  :root {
    --paper: #ffffff;
    --ink: #111111;
    --gold: #cbb85a;
  }
  html, body {
    margin: 0;
    padding: 0;
    width: 720px;
    height: 1200px;
    overflow: hidden;
    background: var(--paper);
  }
  .label {
    position: absolute;
    left: 30px;
    top: 388px;
    width: 660px;
    height: 425px;
    background: var(--paper);
    box-shadow: 0 0 3px rgba(0,0,0,0.35);
  }
  .label svg { display: block; width: 660px; height: 425px; }
  .winery-name { font-family: "Montserrat", sans-serif; font-weight: 400; fill: var(--ink); letter-spacing: 3px; }
  .tagline { font-family: "Montserrat", sans-serif; font-weight: 400; fill: var(--ink); letter-spacing: 1px; }
  .wine-name { font-family: "Montserrat", sans-serif; font-weight: 400; fill: var(--ink); }
  .edition { font-family: "Montserrat", sans-serif; font-weight: 700; fill: var(--paper); }
  .facts { font-family: "Barlow Condensed", sans-serif; fill: var(--ink); text-anchor: middle; }
  .facts-main { font-weight: 500; font-size: 14px; }
  .facts-small { font-weight: 300; font-size: 12px; }
  .facts-tiny { font-weight: 300; font-size: 10px; }
  .facts-bottler { font-weight: 400; font-size: 13px; }
</style>
</head>
<body>
  <div class="label">
    <svg viewBox="0 0 660 425" xmlns="http://www.w3.org/2000/svg">
      <rect class="gold-band" x="330" y="0" width="330" height="44" fill="var(--gold)"/>

      <text class="winery-name" x="322" y="40" font-size="18" text-anchor="end">KELLBERG</text>
      <text class="tagline" x="250" y="67" font-size="12">HANGLAGEN EDITION</text>

      <text class="wine-name" transform="translate(323 351) rotate(-90)" font-size="140" textLength="232" lengthAdjust="spacingAndGlyphs">UNO</text>

      <rect class="edition-box" x="223" y="358" width="100" height="67" fill="var(--ink)"/>
      <text class="edition" x="273" y="393" font-size="17" text-anchor="middle">INICIO</text>

      <g class="facts">
        <text class="facts-main" x="596" y="135">Württemberg</text>
        <text class="facts-main" x="596" y="155">Rotwein</text>
        <text class="facts-main" x="596" y="175">2020</text>
        <text class="facts-small" x="596" y="250">14,5%vol</text>
        <text class="facts-tiny" x="596" y="270">A.P.Nr: 314 772 08</text>
        <text class="facts-bottler" x="596" y="310">Gutsabfüllung</text>
        <text class="facts-bottler" x="596" y="330">Weingut</text>
        <text class="facts-bottler" x="596" y="350">J. Kellberg</text>
      </g>
    </svg>
  </div>
</body>
</html>
```